Business Cards and Stationary for Studio Calmaris (Massage Therapy)
BC for Massage Therapy Studio
Professional
Corwin Palde
President/CEO
742 Fenwick Rd.
Ste. 7C
Alderwick, NV 48213
cpalde@studiocalmaris.example
www.studiocalmaris.example
Logo AI file

```html
<!DOCTYPE html>
<html lang="en">
<head>
<meta charset="utf-8">
<title>Studio Calmaris – Business Card</title>
<link rel="stylesheet" href="https://fonts.googleapis.com/css2?family=Cinzel:wght@400;600&display=swap">
<style>
  :root {
    --page: #e9e7e3;
    --card-top: #2a2a2a;
    --card-bottom: #0d0d0d;
    --accent: #c6cf2c;
    --text: #ffffff;
    --ghost: #242424;
    --ghost-edge: #303030;
  }
  html, body {
    margin: 0;
    width: 1200px;
    height: 778px;
    overflow: hidden;
    background: var(--page);
  }
  .canvas {
    position: relative;
    width: 1200px;
    height: 778px;
  }
  .card {
    position: absolute;
    left: 50px;
    top: 80px;
    width: 1100px;
    height: 618px;
    border-radius: 40px;
    overflow: hidden;
    background: linear-gradient(160deg, var(--card-top) 0%, var(--card-bottom) 70%);
    font-family: "Cinzel", "Times New Roman", serif;
    color: var(--text);
  }
  .ghost-circle {
    position: absolute;
    left: 581px;
    top: 220px;
    width: 520px;
    height: 520px;
    border-radius: 50%;
    background: var(--ghost);
    box-shadow: inset 0 0 0 6px var(--ghost-edge);
  }
  .brand {
    position: absolute;
    left: 0;
    top: 90px;
    width: 550px;
    text-align: center;
  }
  .brand-dot {
    display: block;
    width: 74px;
    height: 74px;
    margin: 0 auto 20px;
    border-radius: 50%;
    background: var(--accent);
  }
  .brand-name {
    display: inline-block;
    margin: 0;
    font-size: 44px;
    font-weight: 400;
    letter-spacing: 1px;
    color: var(--accent);
    line-height: 1.1;
    padding-bottom: 8px;
    border-bottom: 3px solid var(--accent);
  }
  .person {
    position: absolute;
    right: 36px;
    top: 34px;
    text-align: right;
  }
  .person-name {
    margin: 0;
    font-size: 32px;
    font-weight: 400;
    color: var(--accent);
    letter-spacing: 1px;
    line-height: 1.2;
  }
  .person-title {
    margin: 0;
    font-size: 22px;
    color: var(--text);
    letter-spacing: 1px;
  }
  .contact {
    position: absolute;
    left: 67px;
    top: 425px;
    font-size: 20px;
    line-height: 28px;
    letter-spacing: 0.5px;
  }
  .contact p { margin: 0; }
  .contact .gap { margin-top: 6px; }
  .contact-line {
    display: flex;
    align-items: center;
    gap: 8px;
  }
  .contact-line svg {
    width: 15px;
    height: 15px;
    flex: none;
  }
</style>
</head>
<body>
<div class="canvas">
  <section class="card">
    <div class="ghost-circle"></div>

    <div class="brand">
      <span class="brand-dot"></span>
      <h1 class="brand-name">Studio Calmaris</h1>
    </div>

    <div class="person">
      <h2 class="person-name">Corwin Palde</h2>
      <p class="person-title">President/CEO</p>
    </div>

    <div class="contact">
      <p>742 Fenwick Rd., Ste. 7C</p>
      <p>Alderwick, NV 48213</p>
      <p class="contact-line gap">
        <svg viewBox="0 0 16 16" aria-hidden="true"><path d="M4 1 L6.5 4.5 L5 6.5 Q7 10 9.5 11 L11.5 9.5 L15 12 L13 15 Q6 14 1 3 Z" fill="var(--accent)"/></svg>
        555.301.0172
      </p>
      <p class="contact-line">
        <svg viewBox="0 0 16 16" aria-hidden="true"><rect x="1" y="3" width="14" height="10" rx="1" fill="var(--accent)"/><path d="M1.5 3.8 L8 9 L14.5 3.8" stroke="#111" stroke-width="1.3" fill="none"/></svg>
        cpalde@studiocalmaris.example
      </p>
      <p class="contact-line">
        <svg viewBox="0 0 16 16" aria-hidden="true"><circle cx="8" cy="8" r="7" fill="var(--accent)"/><path d="M1 8 H15 M8 1 Q4 8 8 15 M8 1 Q12 8 8 15" stroke="#111" stroke-width="1" fill="none"/></svg>
        www.studiocalmaris.example
      </p>
    </div>
  </section>
</div>
</body>
</html>
```